Lucky Orbit Fun Casino Entertainment

Looking to update my business card and make it look more modern, stand out and eye catching.
We are are fun casino business in Australia (primarily Sydney). Blackjack and Roulette are our most popular games although we have pretty much every game available for hire that you would find in a real casino. The final design would need to be sleek and appeal to the more upmarket corporate sector.
We mainly cater for Corporate Events, Private Parties, Fundraising Events, Team Building, Poker Tournaments
I think I'd prefer the colour Black.

Target Market(s)

High-end Corporate

Industry/Entity Type

Events

Contact Information for Business Card

Dale Hutchins
Director
1300 482 617
0431 758 209
info@luckyorbit.com.au
www.luckyorbit.com.au
Facebook & Instagram @luckyorbitshows (proper social icons preferred)

Colors
000000
0255a3

Requirements
Must have
• Front side:
• Logo
• Contact details
• 'Australia's #1 Fun Casino Specialists'
• Back:
• Logo
Nice to have
• Back:
• Corporate Events
• Private Parties
• Poker Tournaments
• Fundraising
• Props & Theming
• Photo Booth
• Horse Racing Events
• The Vegas Sign attached, maybe on the back of the card in the background...?

```html
<!DOCTYPE html>
<html lang="en">
<head>
<meta charset="utf-8">
<title>Lucky Orbit Fun Casino Entertainment – Business Card</title>
<link href="https://fonts.googleapis.com/css2?family=Montserrat:wght@400;600;800&display=swap" rel="stylesheet">
<style>
  :root {
    --stage: #1b1b1d;
    --card: #2b2b2e;
    --ink-black: #050505;
    --gold: #f6b21f;
    --white: #f2f2f2;
    --blue: #0255a3;
  }
  * { box-sizing: border-box; margin: 0; padding: 0; }
  html, body { width: 1200px; height: 800px; overflow: hidden; }
  body {
    background: var(--stage);
    font-family: "Montserrat", sans-serif;
    color: var(--white);
    position: relative;
  }
  .card {
    position: absolute;
    width: 540px;
    height: 310px;
    background: var(--card);
    overflow: hidden;
    box-shadow: 0 18px 40px rgba(0,0,0,.55);
  }
  .card--front { left: 70px; top: 70px; }
  .card--back { left: 590px; top: 420px; }

  /* front */
  .name-band {
    position: absolute; left: 150px; right: 0; top: 28px; height: 72px;
    background: var(--ink-black);
    padding: 12px 0 0 120px;
  }
  .holder-name { font-weight: 800; font-size: 26px; color: var(--gold); letter-spacing: .5px; line-height: 1.1; }
  .holder-role { font-size: 14px; color: var(--white); margin-top: 2px; }

  .brand-mark {
    position: absolute; left: 18px; top: 48px; width: 180px; height: 180px;
    border-radius: 50%; background: var(--ink-black);
    display: flex; align-items: center; justify-content: center;
  }
  .brand-name {
    font-weight: 800; font-size: 26px; color: var(--gold);
    text-transform: uppercase; text-align: center; line-height: 1.05;
  }

  .contact-list { position: absolute; left: 250px; top: 118px; list-style: none; }
  .contact-list li { display: flex; align-items: center; gap: 8px; font-size: 13.5px; line-height: 20px; }
  .contact-icon { width: 14px; height: 14px; flex: none; }

  .tagline {
    position: absolute; left: 250px; top: 210px;
    color: var(--gold); font-weight: 600; font-size: 17px; line-height: 1.2;
  }

  .social-pill {
    position: absolute; left: 150px; top: 255px; width: 290px; height: 30px;
    background: var(--ink-black); border-radius: 15px;
    display: flex; align-items: center; gap: 6px; padding-left: 8px;
    font-size: 13px;
  }
  .social-dot { width: 18px; height: 18px; border-radius: 50%; background: var(--gold); flex: none; }
  .social-handle { margin-left: 8px; }

  /* back */
  .back-panel {
    position: absolute; left: 0; top: 0; width: 215px; height: 100%;
    background: var(--ink-black);
  }
  .back-mark {
    position: absolute; left: 30px; top: 45px; width: 220px; height: 220px;
    border-radius: 50%; background: var(--ink-black);
    border: 6px solid #111;
    display: flex; align-items: center; justify-content: center;
  }
  .back-mark .brand-name { font-size: 32px; }

  .service-title {
    position: absolute; left: 290px; top: 40px;
    color: var(--gold); font-weight: 600; font-size: 17px; letter-spacing: .5px;
  }
  .service-list { position: absolute; left: 290px; top: 72px; list-style: none; }
  .service-list li { display: flex; align-items: center; gap: 10px; font-size: 14px; line-height: 22px; }
  .service-dot {
    width: 13px; height: 13px; border-radius: 50%;
    background: var(--blue); border: 2px dashed var(--white); flex: none;
  }
  .web-pill {
    position: absolute; left: 285px; top: 258px; width: 255px; height: 30px;
    background: var(--ink-black); border-radius: 15px 0 0 15px;
    color: var(--gold); font-size: 13.5px; font-weight: 600;
    display: flex; align-items: center; padding-left: 16px;
  }
</style>
</head>
<body>

<section class="card card--front" aria-label="Business card front">
  <div class="name-band">
    <p class="holder-name">DALE HUTCHINS</p>
    <p class="holder-role">Director</p>
  </div>

  <div class="brand-mark">
    <p class="brand-name">Lucky<br>Orbit</p>
  </div>

  <ul class="contact-list">
    <li>
      <svg class="contact-icon" viewBox="0 0 14 14" aria-hidden="true"><circle cx="7" cy="7" r="7" fill="var(--gold)"/><path d="M4.5 3.5l1.5 0 .6 2-1 .8c.5 1 1.2 1.7 2.1 2.1l.8-1 2 .6v1.5c-3.5.3-6.3-2.5-6-6z" fill="#000"/></svg>
      1300 482 617
    </li>
    <li>
      <svg class="contact-icon" viewBox="0 0 14 14" aria-hidden="true"><circle cx="7" cy="7" r="7" fill="var(--gold)"/><rect x="5" y="3" width="4" height="8" rx="1" fill="#000"/></svg>
      0431 758 209
    </li>
    <li>
      <svg class="contact-icon" viewBox="0 0 14 14" aria-hidden="true"><circle cx="7" cy="7" r="7" fill="var(--gold)"/><rect x="3.5" y="4.5" width="7" height="5" fill="#000"/><path d="M3.5 4.5l3.5 3 3.5-3" stroke="var(--gold)" stroke-width=".8" fill="none"/></svg>
      info@luckyorbit.com.au
    </li>
    <li>
      <svg class="contact-icon" viewBox="0 0 14 14" aria-hidden="true"><circle cx="7" cy="7" r="7" fill="var(--gold)"/><circle cx="7" cy="7" r="3.6" fill="none" stroke="#000" stroke-width="1"/><path d="M3.4 7h7.2M7 3.4c-1.6 2-1.6 5.2 0 7.2M7 3.4c1.6 2 1.6 5.2 0 7.2" stroke="#000" stroke-width=".8" fill="none"/></svg>
      www.luckyorbit.com.au
    </li>
  </ul>

  <p class="tagline">Australia's #1<br>Fun Casino Specialists</p>

  <div class="social-pill" aria-label="Social media handle">
    <span class="social-dot" aria-hidden="true"></span>
    <span class="social-dot" aria-hidden="true"></span>
    <span class="social-handle">@luckyorbitshows</span>
  </div>
</section>

<section class="card card--back" aria-label="Business card back">
  <div class="back-panel"></div>
  <div class="back-mark">
    <p class="brand-name">Lucky<br>Orbit</p>
  </div>

  <h2 class="service-title">OUR SERVICE</h2>
  <ul class="service-list">
    <li><span class="service-dot"></span>Corporate Events</li>
    <li><span class="service-dot"></span>Private Parties</li>
    <li><span class="service-dot"></span>Poker Tournaments</li>
    <li><span class="service-dot"></span>Fundraising</li>
    <li><span class="service-dot"></span>Props &amp; Theming</li>
    <li><span class="service-dot"></span>Photo Booth</li>
    <li><span class="service-dot"></span>Horse Racing Events</li>
  </ul>

  <div class="web-pill">www.luckyorbit.com.au</div>
</section>

</body>
</html>
```